Business Card Design Project

Financial planning, Insurance and Real estate - Financial Services company

Contact Information for Business Card

Looking for something simple in design -
Brindlewood Capital LLC
Brindlewood Wealth Managment

```html
<!DOCTYPE html>
<html lang="en">
<head>
<meta charset="utf-8">
<title>Brindlewood Wealth Management – Business Card</title>
<link href="https://fonts.googleapis.com/css2?family=Archivo:wght@800&family=Oxygen:wght@400&display=swap" rel="stylesheet">
<style>
  :root {
    --backdrop: #3a3a3c;
    --card: #1f1a20;
    --brand-blue: #1a86c8;
    --text-grey: #b9b9bd;
    --label-grey: #9c9ca2;
  }
  * { box-sizing: border-box; margin: 0; padding: 0; }
  html, body {
    width: 1200px; height: 900px; overflow: hidden;
    background: var(--backdrop);
  }
  .canvas {
    width: 1200px; height: 900px;
    display: flex; flex-direction: column; align-items: center; justify-content: center;
    gap: 40px;
  }
  .card {
    width: 700px; height: 400px;
    background: var(--card);
    border-radius: 24px;
    position: relative;
    box-shadow: 0 10px 24px rgba(0,0,0,.45);
  }
  .wordmark {
    display: flex; align-items: center; gap: 12px;
    font-family: "Archivo", "Arial Black", sans-serif;
    font-weight: 800;
    color: var(--brand-blue);
    line-height: 1.05;
  }
  .wordmark-dot {
    width: 14px; height: 14px; border-radius: 50%;
    background: var(--brand-blue); flex: none;
  }
  /* Front */
  .card-front { display: flex; align-items: center; justify-content: center; }
  .card-front .wordmark { font-size: 24px; margin-top: 40px; }
  /* Back */
  .card-back { display: flex; align-items: center; }
  .card-back .brand-block {
    width: 330px; height: 100%;
    display: flex; align-items: flex-end; justify-content: center;
    padding-bottom: 110px;
  }
  .card-back .wordmark { font-size: 30px; }
  .card-back .wordmark small { display: block; font-size: 16px; letter-spacing: .02em; }
  .divider {
    width: 2px; height: 280px; background: var(--brand-blue); flex: none;
  }
  .contact {
    padding-left: 48px;
    font-family: "Oxygen", sans-serif;
    color: var(--text-grey);
  }
  .person-name {
    font-family: "Archivo", "Arial Black", sans-serif;
    font-weight: 800; font-size: 20px; color: var(--brand-blue);
  }
  .person-role {
    font-family: "Archivo", "Arial Black", sans-serif;
    font-weight: 800; font-size: 12px; letter-spacing: .04em;
    color: var(--label-grey); margin: 4px 0 18px 8px;
  }
  .contact-list { list-style: none; }
  .contact-list li {
    display: flex; align-items: center; gap: 10px;
    font-size: 18px; line-height: 1.35; white-space: nowrap;
  }
  .contact-list svg { width: 15px; height: 15px; fill: var(--brand-blue); flex: none; }
  .contact-group { margin-bottom: 12px; }
  .address { font-size: 18px; line-height: 1.25; margin-left: 25px; margin-top: 18px; }
</style>
</head>
<body>
<main class="canvas">
  <section class="card card-front" aria-label="Card front">
    <p class="wordmark"><span class="wordmark-dot"></span>Brindlewood Wealth Management</p>
  </section>

  <section class="card card-back" aria-label="Card back">
    <div class="brand-block">
      <p class="wordmark"><span class="wordmark-dot"></span><span>Brindlewood<small>WEALTH MANAGEMENT</small></span></p>
    </div>
    <div class="divider"></div>
    <div class="contact">
      <p class="person-name">Daniel Harrow</p>
      <p class="person-role">MANAGING DIRECTOR</p>
      <ul class="contact-list contact-group">
        <li><svg viewBox="0 0 16 16" aria-hidden="true"><path d="M4 0h8a1 1 0 0 1 1 1v14a1 1 0 0 1-1 1H4a1 1 0 0 1-1-1V1a1 1 0 0 1 1-1zm1 2v10h6V2zm3 11a1 1 0 1 0 0 2 1 1 0 0 0 0-2z"/></svg>555 210 48 36</li>
        <li><svg viewBox="0 0 16 16" aria-hidden="true"><path d="M3.5 1l2.5 3-1.5 2c1 2 2.5 3.5 4.5 4.5l2-1.5 3 2.5-1.5 2.5C7 14 2 9 1 2.5z"/></svg>888 402 17 90</li>
      </ul>
      <ul class="contact-list">
        <li><svg viewBox="0 0 16 16" aria-hidden="true"><path d="M0 3h16v1L8 9 0 4zm0 3l8 5 8-5v7H0z"/></svg>d.harrow@brindlewood-wm.com</li>
        <li><svg viewBox="0 0 16 16" aria-hidden="true"><path d="M8 0a8 8 0 1 0 0 16A8 8 0 0 0 8 0zm-1 1.6V5H4.2A6.5 6.5 0 0 1 7 1.6zm2 0A6.5 6.5 0 0 1 11.8 5H9zM1.6 7H7v2H1.6a6.5 6.5 0 0 1 0-2zM9 7h5.4a6.5 6.5 0 0 1 0 2H9zM4.2 11H7v3.4A6.5 6.5 0 0 1 4.2 11zM9 11h2.8A6.5 6.5 0 0 1 9 14.4z"/></svg>www.brindlewood-wm.com</li>
      </ul>
      <p class="address">48 Alder Lane, Millbrook<br>New York 10562</p>
    </div>
  </section>
</main>
</body>
</html>
```